Website for new dental office

I am Dr. Colin Marsh and am building a new dental practice. I specialize in general dentistry. I am young and have a higher end dental practice incorporating very new technologies and would like my website to reflect that. As many dental patients are older, the website must be very easy to navigate. I would like patients to be able to request appointments, and will eventually add on patient information forms (the health history, etc, that you normally fill out in the practice) from my practice management software, so leave an area for that.

Industry/Entity Type

Building

```html
<!DOCTYPE html>
<html lang="en">
<head>
<meta charset="utf-8">
<title>Dr. Colin Marsh, DDS</title>
<link rel="stylesheet" href="https://fonts.googleapis.com/css2?family=Oswald:wght@400;500&family=Roboto:ital,wght@0,400;0,500;0,700;1,400&family=Patrick+Hand&display=swap">
<style>
:root{
  --green:#4a9a28;
  --green-bright:#5cb531;
  --ink:#2b2b2b;
  --text:#555;
  --blue:#2a7db5;
  --navy:#1d3b6b;
  --bar:#333;
  --line:#d9d9d9;
  --foot:#fafaf8;
}
*{box-sizing:border-box;margin:0;padding:0}
html,body{width:1106px;height:1200px;overflow:hidden;background:#fff}
body{font-family:"Roboto",sans-serif;color:var(--text);position:relative}
a{color:inherit;text-decoration:none}
.abs{position:absolute}

/* wordmark: one colour, one weight of the text font */
.wordmark{font-family:"Roboto",sans-serif;font-weight:500;color:var(--green);white-space:nowrap;letter-spacing:0}
.site-brand{left:157px;top:30px;font-size:28px}
.foot-brand{left:0;top:24px;width:1106px;text-align:center;font-size:28px}

/* header */
.header-phone{left:818px;top:18px;font:500 15px "Roboto",sans-serif;color:var(--ink);display:flex;align-items:center;gap:6px}
.main-nav{left:453px;top:54px;width:483px;height:26px;display:flex;justify-content:space-between;padding:0 0 0 10px;border-bottom:4px solid #111}
.main-nav a{font:400 15px "Oswald",sans-serif;color:var(--ink);position:relative;white-space:nowrap}
.main-nav a.active::after{content:"";position:absolute;left:-10px;right:-10px;bottom:-8px;height:4px;background:var(--green)}

/* hero */
.hero{left:0;top:98px;width:1106px;height:400px;overflow:hidden}
.hero-photo{position:absolute;inset:0;background:linear-gradient(180deg,#c9d3d9 0%,#aebcc4 35%,#8b8470 60%,#7a6e5c 100%)}
.hero-photo::after{content:"";position:absolute;left:560px;top:0;width:420px;height:400px;background:radial-gradient(ellipse at 50% 60%,rgba(245,240,232,.85),rgba(245,240,232,0) 70%)}
.hero-title{left:176px;top:120px;font:400 44px/54px "Patrick Hand",cursive;color:#3a3530;text-shadow:1px 2px 3px rgba(0,0,0,.35)}
.hero-arrow{top:166px;width:52px;height:120px;background:rgba(255,255,255,.92)}
.hero-arrow.prev{left:78px;border-radius:0 60px 60px 0}
.hero-arrow.next{left:976px;border-radius:60px 0 0 60px}
.hero-arrow svg{position:absolute;top:45px}
.hero-dots{left:175px;top:348px;display:flex;gap:7px}
.hero-dots span{width:15px;height:15px;border-radius:50%;background:#ddd;border:1px solid #bbb}
.hero-dots span.on{background:var(--green-bright)}
.hero-curve{left:0;top:460px}

/* about */
.about-title{left:0;top:492px;width:1106px;display:flex;justify-content:center;align-items:center;gap:18px;font:400 30px "Oswald",sans-serif;color:var(--ink)}
.about-title .name{color:var(--green)}
.about-title::before,.about-title::after{content:"";width:60px;height:2px;margin-top:14px;background:linear-gradient(90deg,transparent,#bbb)}
.about-title::after{transform:scaleX(-1)}
.about-text{left:160px;top:540px;width:786px;font-size:13px;line-height:20px;text-align:center;color:#666}
.read-more{left:0;top:590px;width:1106px;text-align:center;font:500 11px "Roboto",sans-serif;color:var(--blue)}
.divider{left:240px;top:632px;width:626px;height:8px;background:radial-gradient(ellipse at 50% 0,rgba(0,0,0,.16),rgba(0,0,0,0) 70%)}

/* panels */
.panel{top:667px;width:236px;height:197px;border:1px solid var(--line);border-bottom:3px solid var(--green);padding:10px 16px}
.panel h3{font:400 16px "Oswald",sans-serif;color:var(--ink);margin-bottom:8px}
.panel h3 span{color:var(--green)}
.services{left:176px}
.services h4{font:500 11px "Roboto",sans-serif;color:var(--ink);text-decoration:underline;margin-bottom:3px}
.services p{font:italic 10.5px/18px "Roboto",sans-serif;color:#444;margin-bottom:8px}
.services p a{color:var(--green)}
.btn{display:inline-block;background:var(--blue);color:#fff;font:500 10.5px "Roboto",sans-serif;letter-spacing:.3px;padding:4px 14px;border-radius:2px}
.testimonials{left:438px}
.testi-nav{position:absolute;right:18px;top:14px}
.testimonials blockquote{font:italic 10.5px/18px "Roboto",sans-serif;color:#444}
.testimonials cite{display:block;font:700 12px "Roboto",sans-serif;font-style:normal;color:var(--navy);margin-top:4px}
.testimonials .role{font-size:11px;color:#777}
.lab{left:700px}
.lab form{position:absolute;left:18px;top:36px}
.lab input,.lab textarea{display:block;width:202px;border:1px solid #ccc;box-shadow:inset 0 1px 2px rgba(0,0,0,.08);font:italic 10px "Roboto",sans-serif;padding:3px 8px;margin:0 0 6px;color:#777;background:#fff}
.lab input{height:20px}
.lab textarea{height:50px;resize:none}
.lab .submit{position:absolute;right:14px;top:170px;background:var(--blue);color:#fff;border:0;border-radius:5px;font:500 12px "Roboto",sans-serif;padding:3px 12px}

/* gallery */
.gallery{left:176px;top:901px;width:497px;height:90px;border:1px solid var(--line)}
.gallery .thumb{position:absolute;top:6px;width:103px;height:78px}
.gallery .g-arrow{position:absolute;top:28px}
.call-box{left:700px;top:916px;width:236px;height:61px;border:1px solid var(--line);padding:5px}
.call-inner{background:var(--blue);height:49px;border-radius:2px;display:flex;align-items:center;gap:12px;padding-left:20px;color:#fff}
.call-inner div{font:500 16px/19px "Roboto",sans-serif}
.call-inner strong{font-size:20px;font-weight:700}

/* newsletter bar */
.news-bar{left:0;top:1011px;width:1106px;height:43px;background:var(--bar);color:#fff;font-size:11.5px}
.news-label{left:175px;top:12px;display:flex;align-items:center;gap:9px}
.news-form{left:318px;top:13px;display:flex}
.news-form input{width:170px;height:18px;border:0;font:italic 10px "Roboto",sans-serif;color:#999;padding:0 7px}
.news-form button{height:18px;border:0;background:var(--blue);color:#fff;font:500 10px "Roboto",sans-serif;padding:0 8px}
.social{left:693px;top:9px;display:flex;align-items:center;gap:8px}
.social span.label{margin-right:4px}
.social i{display:block;width:24px;height:24px;border-radius:2px;background:#555}
.social i.share{background:var(--green)}

/* footer */
.footer{left:0;top:1054px;width:1106px;height:146px;background:var(--foot)}
.foot-nav{left:0;top:74px;width:1106px;text-align:center;font-size:12px;color:#222}
.foot-nav a{margin:0 8px}
.foot-nav b{font-weight:400;color:#555}
.foot-copy{left:0;top:100px;width:1106px;text-align:center;font-size:10.5px;color:#444;line-height:21px}
</style>
</head>
<body>

<header>
  <div class="abs wordmark site-brand">Dr. Colin Marsh, DDS</div>
  <div class="abs header-phone">
    <svg width="20" height="22" viewBox="0 0 20 22" aria-hidden="true"><path d="M4 1c1.5-.5 2.5 0 3 1.5l1.2 3.5c.3 1-.2 1.8-1 2.3l-1.2.8c1 3 2.8 5.4 5.5 7.2l1.1-1c.8-.6 1.7-.7 2.5 0l2.8 2.4c1 1 1 2-.2 3-1.7 1.4-3.8 1.5-6 0C6.5 17.5 2.8 12.4 1.5 7 1 4.3 2 2 4 1z" fill="#2a8fc4"/></svg>
    555-014-2368
  </div>
  <nav class="abs main-nav">
    <a class="active" href="#">Home</a><a href="#">Team</a><a href="#">Services</a><a href="#">Portfolio</a><a href="#">Our Office</a><a href="#">Patient Resources</a><a href="#">Contact Us</a>
  </nav>
</header>

<section class="abs hero">
  <div class="hero-photo" role="img" aria-label="Photo of a smiling family walking barefoot along a sandy beach by the sea"></div>
  <h1 class="abs hero-title">Lorem ipsum dolor sit<br>amet Lorem ipsum</h1>
  <a class="abs hero-arrow prev" href="#" aria-label="Previous slide"><svg width="26" height="34" viewBox="0 0 26 34" style="left:2px"><path d="M20 3 6 17l14 14" fill="none" stroke="#3b3540" stroke-width="7"/></svg></a>
  <a class="abs hero-arrow next" href="#" aria-label="Next slide"><svg width="26" height="34" viewBox="0 0 26 34" style="left:24px"><path d="M6 3l14 14L6 31" fill="none" stroke="#3b3540" stroke-width="7"/></svg></a>
  <div class="abs hero-dots"><span></span><span class="on"></span><span></span><span></span></div>
</section>
<svg class="abs hero-curve" width="1106" height="40" viewBox="0 0 1106 40" aria-hidden="true">
  <path d="M0 38V33C300 5 800 5 1106 32V40H0z" fill="#fff"/>
  <path d="M0 33C300 5 800 5 1106 32" fill="none" stroke="#5cb531" stroke-width="4"/>
</svg>

<section>
  <h2 class="abs about-title"><span>About <span class="name">Dr. Colin Marsh</span></span></h2>
  <p class="abs about-text">Lorem ipsum dolor sit amet, consectetuer adipiscing elit, sed diam nonummy nibhLorem ipsum dolor sit amet, consectetuer adipiscing elit, sed diam nonummy nibhLorem ipsum dolor sit amet, consectetuer adipiscing elit, sed diam nonummy nibh...</p>
  <a class="abs read-more" href="#">READ MORE { + }</a>
  <div class="abs divider"></div>
</section>

<section class="abs panel services">
  <h3>Our <span>Services</span></h3>
  <h4>Dental Implants</h4>
  <p>Lorem ipsum dolor sit amet, Lorem The Lorem&nbsp; consectetuer adipiscing..<a href="#">More&gt;</a></p>
  <h4>Cosmetics</h4>
  <p>Lorem ipsum dolor sit amet, Lorem The Lorem&nbsp; consectetuer adipiscing elit..<a href="#">More&gt;</a></p>
  <a class="btn" href="#">VIEW ALL</a>
</section>

<section class="abs panel testimonials">
  <h3>Client <span>Testimonials</span></h3>
  <svg class="testi-nav" width="28" height="12" viewBox="0 0 28 12" aria-hidden="true"><path d="M7 1 2 6l5 5M21 1l5 5-5 5" fill="none" stroke="#777" stroke-width="2.5"/></svg>
  <blockquote>
    <svg width="18" height="14" viewBox="0 0 18 14" style="vertical-align:-1px" aria-hidden="true"><path d="M0 14V8C0 3 3 0 7 0v3C5 3 4 5 4 7h3v7zM10 14V8c0-5 3-8 7-8v3c-2 0-3 2-3 4h3v7z" fill="#ccc"/></svg>
    Lorem ipsum dolor sit amet, Lorem The Lorem&nbsp; consectetuer adipiscing elit, sed diam nonummy nibh Lorem Lorem ipsum dolor sit amet, Lorem The Lorem This The consectetuer adipiscing elit, sed diam nonummy nibh Lorem
    <svg width="18" height="14" viewBox="0 0 18 14" style="vertical-align:-8px;margin-left:4px" aria-hidden="true"><path d="M18 0v6c0 5-3 8-7 8v-3c2 0 3-2 3-4h-3V0zM8 0v6c0 5-3 8-7 8v-3c2 0 3-2 3-4H1V0z" fill="#ccc"/></svg>
  </blockquote>
  <cite>Lorem ipsum</cite>
  <div class="role">Lorem ipsum</div>
</section>

<section class="abs panel lab">
  <h3>Request <span>Lab Services</span></h3>
  <form>
    <input type="text" placeholder="Name">
    <input type="text" placeholder="Phone">
    <input type="text" placeholder="Email">
    <textarea placeholder="Message"></textarea>
    <button class="submit" type="button">Submit</button>
  </form>
</section>

<section class="abs gallery">
  <svg class="g-arrow" width="10" height="32" viewBox="0 0 10 32" style="left:10px" aria-hidden="true"><path d="M10 0v32L0 16z" fill="#666"/></svg>
  <div class="thumb" style="left:31px;background:linear-gradient(180deg,#9a2a2a,#c97a6a 50%,#8a2222)" role="img" aria-label="Before photo of teeth with gaps"></div>
  <div class="thumb" style="left:141px;background:linear-gradient(180deg,#a83a38,#e8dcc8 50%,#9a3030)" role="img" aria-label="After photo of restored smile"></div>
  <div class="thumb" style="left:251px;background:linear-gradient(135deg,#dfe6e8,#d8b9a4 60%,#c99a88)" role="img" aria-label="Cosmetic injection treatment photo"></div>
  <div class="thumb" style="left:361px;background:linear-gradient(135deg,#f2f2f2,#e6d2c6 60%,#d3b4a6)" role="img" aria-label="Facial skin care treatment photo"></div>
  <svg class="g-arrow" width="10" height="32" viewBox="0 0 10 32" style="left:477px" aria-hidden="true"><path d="M0 0v32l10-16z" fill="#666"/></svg>
</section>

<aside class="abs call-box">
  <div class="call-inner">
    <svg width="34" height="34" viewBox="0 0 34 34" aria-hidden="true"><circle cx="17" cy="17" r="15" fill="none" stroke="#fff" stroke-width="2.5"/><path d="M12 8c1-.3 1.7 0 2 1l1 3c.2.7-.1 1.2-.6 1.5l-.8.5c.7 2.4 2 4.3 4 5.8l.8-.7c.5-.4 1.1-.5 1.7 0l2 1.8c.7.6.6 1.3-.1 1.9-1.2 1-2.7 1-4.2 0-3.6-2.3-6-6-6.8-9.6-.3-1.8.3-3.4 1-4.2z" fill="#fff"/></svg>
    <div>Call Us Today<br><strong>555-014-2368</strong></div>
  </div>
</aside>

<section class="abs news-bar">
  <div class="abs news-label">
    <svg width="24" height="18" viewBox="0 0 24 18" aria-hidden="true"><path d="M1 7 12 0l11 7v11H1z" fill="#ddd"/><path d="M1 7l11 7 11-7" fill="none" stroke="#888" stroke-width="1.2"/></svg>
    Newsletter sign up
  </div>
  <form class="abs news-form"><input type="text" placeholder="email address"><button type="button">SUBMIT</button></form>
  <div class="abs social">
    <span class="label">Connect with us</span>
    <i class="share"></i><i></i><i></i><i></i><i></i>
  </div>
</section>

<footer class="abs footer">
  <div class="abs wordmark foot-brand">Dr. Colin Marsh, DDS</div>
  <nav class="abs foot-nav">
    <a href="#">Home</a><b>I</b><a href="#">Team</a><b>I</b><a href="#">Services</a><b>I</b><a href="#">Portfolio</a><b>I</b><a href="#">Our Office</a><b>I</b><a href="#">Patient Resources</a><b>I</b><a href="#">Contact Us</a>
  </nav>
  <div class="abs foot-copy">© 2014 DrColinMarsh. All Rights Reserved<br>Phone : 555-014-2368 |&nbsp; Fax : 555-014-2369</div>
</footer>

</body>
</html>
```